Chauffeur Service Presentation folder with 4 side flyer

Things to consider when creating the design,
- I do not want it to look like my old brochure which looks boring and relates to the industry for example we don’t need to use pictures of cars or pictures of a Chauffeur opening a door. etc… Just want it to look modern and creative. Something simple and minimalisitic. If you have any ideas I am happy to let you suggest something.

PRESENTATION FOLDER
-Presentation folder will be prepared to fit A4 size flyer into the inside sleeve.
Clean and simple look. FILE 1 ""EXAMPLE OF FOLDER.PNG""
like the clean look of this folder FILE 4 "EXAMPLE OF FOLDER 2""

-would prefer to use white as the main color

Trying to maintain a similar colour pallet as my company pallet.
FILE 2 ""CHAUFFEURED COLOR PALLETE""

-BROCHURE FLYER

- will fit into the internal sleeve of presentation folder, will need 4 sides to to the flyer with 1 fold. example
FILE 8 "'BROCHURE FOLDED ""

-I have also attached the old brochure we had which is really outdated, just a guide for you to see what we had. FILE 3 ""PROFILE 2013 TKPORTAL""

-Relate to the color scheme we have used for Logo and business card attached in color palette. I have higher res for you if you want me to forward to you.

-Could use some illustration/ icons in the place of images for service provided etc,
FILE 5 ""IDEA FOR SERVICE TYPES""

Listing my service types like below on front page or inside there flyer or even on the presentation folder?
FILE 6 ""LIST OF SERVICES""
Corporate transfer, Airport transfer, vip service, door to door service,
I can provide a list to create

The Layout inside, I am not to fussed as long as it is clean looking,
Maybe we can use the business color scheme throughout while changing font colors and make some parts inversed by using white text with the color boxed over it?

example of white text with coloured box and also different types of font
FILE 7 ""IDEAS""

```html
<!DOCTYPE html>
<html lang="en">
<head>
<meta charset="utf-8">
<title>Velmont – Presentation Folder Covers</title>
<link rel="stylesheet" href="https://fonts.googleapis.com/css2?family=Open+Sans:wght@400;600&display=swap">
<style>
  :root {
    --backdrop: #e9e6e2;
    --cover-red: #b3394d;
    --cover-red-deep: #a8344a;
    --cover-stone: #b0a79d;
    --cover-stone-deep: #a79e94;
    --cover-charcoal: #3d3d3f;
    --cover-charcoal-deep: #353537;
    --band: #414143;
    --accent: #e5485f;
    --white: #ffffff;
  }
  * { box-sizing: border-box; margin: 0; padding: 0; }
  html, body { width: 1200px; height: 1200px; overflow: hidden; }
  body {
    background: var(--backdrop);
    font-family: "Open Sans", sans-serif;
    position: relative;
  }
  .cover {
    position: absolute;
    width: 416px;
    height: 570px;
    box-shadow: 0 4px 14px rgba(0,0,0,.25);
  }
  .cover--red { left: 130px; top: 30px; background: linear-gradient(180deg, var(--cover-red), var(--cover-red-deep)); }
  .cover--stone { left: 627px; top: 30px; background: linear-gradient(180deg, var(--cover-stone), var(--cover-stone-deep)); }
  .cover--charcoal { left: 373px; top: 616px; background: linear-gradient(180deg, var(--cover-charcoal), var(--cover-charcoal-deep)); }

  .brand-name {
    position: absolute;
    left: 0; right: 0; top: 212px;
    text-align: center;
    font-weight: 600;
    font-size: 58px;
    letter-spacing: 1px;
    color: var(--white);
  }
  .tagline {
    position: absolute;
    left: 0; right: 0; top: 455px;
    text-align: center;
    font-size: 13.5px;
    font-weight: 400;
    color: var(--white);
  }
  .cover--stone .tagline,
  .cover--charcoal .tagline { color: var(--accent); }

  .service-band {
    position: absolute;
    left: 0; right: 0; top: 485px;
    height: 40px;
    background: var(--band);
    border-top: 2px solid var(--accent);
    border-bottom: 2px solid var(--accent);
    display: flex;
    justify-content: center;
    align-items: center;
    gap: 9px;
  }
  .cover--red .service-band { border-color: #d3596b; }
  .cover--charcoal .service-band {
    background: linear-gradient(180deg, #4a4a4c, #3a3a3c);
  }
  .service-icon { width: 27px; height: 27px; display: block; }

  .web-address {
    position: absolute;
    left: 0; right: 0; top: 541px;
    text-align: center;
    font-size: 8.5px;
    letter-spacing: 1.6px;
    color: #f1d5da;
  }
  .cover--stone .web-address,
  .cover--charcoal .web-address { color: var(--accent); }
</style>
</head>
<body>

<svg width="0" height="0" style="position:absolute" aria-hidden="true">
  <defs>
    <symbol id="icon-briefcase" viewBox="0 0 27 27">
      <rect x="1" y="1" width="25" height="25" rx="3" fill="none" stroke="#e5485f" stroke-width="1.6"/>
      <rect x="6" y="10" width="15" height="10" rx="1.5" fill="#e5485f"/>
      <rect x="10.5" y="7" width="6" height="3" rx="1" fill="none" stroke="#e5485f" stroke-width="1.4"/>
    </symbol>
    <symbol id="icon-car" viewBox="0 0 27 27">
      <rect x="1" y="1" width="25" height="25" rx="3" fill="none" stroke="#e5485f" stroke-width="1.6"/>
      <path d="M8 12 L9.5 8 H17.5 L19 12 Z" fill="none" stroke="#e5485f" stroke-width="1.4"/>
      <rect x="6" y="12" width="15" height="6" rx="1.5" fill="#e5485f"/>
      <rect x="7" y="18" width="3" height="2.5" fill="#e5485f"/>
      <rect x="17" y="18" width="3" height="2.5" fill="#e5485f"/>
    </symbol>
    <symbol id="icon-plane" viewBox="0 0 27 27">
      <rect x="1" y="1" width="25" height="25" rx="3" fill="none" stroke="#e5485f" stroke-width="1.6"/>
      <path d="M13.5 5 L14.8 11.5 L21.5 14.5 L21.5 16 L14.8 14.3 L14.4 19.5 L16.5 21 L16.5 22 L13.5 21.2 L10.5 22 L10.5 21 L12.6 19.5 L12.2 14.3 L5.5 16 L5.5 14.5 L12.2 11.5 Z" fill="#e5485f"/>
    </symbol>
    <symbol id="icon-clock" viewBox="0 0 27 27">
      <rect x="1" y="1" width="25" height="25" rx="3" fill="none" stroke="#e5485f" stroke-width="1.6"/>
      <circle cx="13.5" cy="13.5" r="7.5" fill="none" stroke="#e5485f" stroke-width="1.4"/>
      <path d="M13.5 9 V13.5 H17" fill="none" stroke="#e5485f" stroke-width="1.4"/>
    </symbol>
  </defs>
</svg>

<section class="cover cover--red">
  <h1 class="brand-name">Velmont</h1>
  <p class="tagline">THE LEADER IN CHAUFFEUR DRIVEN SERVICES</p>
  <div class="service-band">
    <svg class="service-icon" aria-label="Corporate transfer"><use href="#icon-briefcase"/></svg>
    <svg class="service-icon" aria-label="Door to door service"><use href="#icon-car"/></svg>
    <svg class="service-icon" aria-label="Airport transfer"><use href="#icon-plane"/></svg>
    <svg class="service-icon" aria-label="On time service"><use href="#icon-clock"/></svg>
  </div>
  <p class="web-address">www.velmontdrive.com.au</p>
</section>

<section class="cover cover--stone">
  <h1 class="brand-name">Velmont</h1>
  <p class="tagline">THE LEADER IN CHAUFFEUR DRIVEN SERVICES</p>
  <div class="service-band">
    <svg class="service-icon" aria-label="Corporate transfer"><use href="#icon-briefcase"/></svg>
    <svg class="service-icon" aria-label="Door to door service"><use href="#icon-car"/></svg>
    <svg class="service-icon" aria-label="Airport transfer"><use href="#icon-plane"/></svg>
    <svg class="service-icon" aria-label="On time service"><use href="#icon-clock"/></svg>
  </div>
  <p class="web-address">www.velmontdrive.com.au</p>
</section>

<section class="cover cover--charcoal">
  <h1 class="brand-name">Velmont</h1>
  <p class="tagline">THE LEADER IN CHAUFFEUR DRIVEN SERVICES</p>
  <div class="service-band">
    <svg class="service-icon" aria-label="Corporate transfer"><use href="#icon-briefcase"/></svg>
    <svg class="service-icon" aria-label="Door to door service"><use href="#icon-car"/></svg>
    <svg class="service-icon" aria-label="Airport transfer"><use href="#icon-plane"/></svg>
    <svg class="service-icon" aria-label="On time service"><use href="#icon-clock"/></svg>
  </div>
  <p class="web-address">www.velmontdrive.com.au</p>
</section>

</body>
</html>
```